Stationery Design Project

Minimal Design. Black and White Colours Only.
Need Business Card
With Compliments slip
Letterhead
A4 Folder

Target Market(s)

Luxury architectual designed home owners

Industry/Entity Type

Business

Requirements
Must have
• Black and White colours only. Suggest some good textured stock for business card for future printing. try to use font that is used in my logo our some other minimal modern font.

```html
<!DOCTYPE html>
<html lang="en">
<head>
<meta charset="utf-8">
<title>Kalder Estates — Business Card</title>
<link rel="stylesheet" href="https://fonts.googleapis.com/css2?family=Inter:wght@400;500&display=swap">
<style>
  :root {
    --paper: #ffffff;
    --ink: #000000;
    --backdrop: #ececec;
    --band-text: #ffffff;
  }
  html, body {
    margin: 0;
    padding: 0;
    width: 1200px;
    height: 1000px;
    overflow: hidden;
    background: var(--backdrop);
    font-family: "Inter", Arial, sans-serif;
  }
  .business-card {
    position: absolute;
    left: 242px;
    top: 281px;
    width: 716px;
    height: 437px;
    background: var(--paper);
    color: var(--ink);
  }
  .brand-mark {
    position: absolute;
    left: 124px;
    top: 134px;
    width: 70px;
    height: 70px;
    background: var(--ink);
  }
  .brand-name {
    position: absolute;
    left: 235px;
    top: 148px;
    margin: 0;
    font-size: 41px;
    font-weight: 500;
    line-height: 1;
    letter-spacing: 0.2px;
    white-space: nowrap;
  }
  .holder-name {
    position: absolute;
    left: 246px;
    top: 210px;
    margin: 0;
    font-size: 35px;
    font-weight: 400;
    line-height: 1;
    white-space: nowrap;
  }
  .holder-role {
    position: absolute;
    left: 246px;
    top: 251px;
    margin: 0;
    font-size: 23px;
    font-weight: 400;
    line-height: 1;
    white-space: nowrap;
  }
  .rule {
    position: absolute;
    top: 263px;
    height: 3px;
    background: var(--ink);
  }
  .rule--left { left: 13px; width: 216px; }
  .rule--right { left: 481px; width: 220px; }
  .contact-band {
    position: absolute;
    left: 0;
    top: 369px;
    width: 716px;
    height: 68px;
    background: var(--ink);
    color: var(--band-text);
    font-size: 14.5px;
    line-height: 17px;
  }
  .contact-address {
    position: absolute;
    left: 12px;
    top: 8px;
    width: 180px;
    text-align: center;
    font-style: normal;
  }
  .contact-lines {
    position: absolute;
    right: 14px;
    top: 8px;
    text-align: right;
  }
  .contact-lines div, .contact-address div { white-space: nowrap; }
</style>
</head>
<body>
  <article class="business-card">
    <span class="brand-mark" aria-hidden="true"></span>
    <h1 class="brand-name">KALDER ESTATES</h1>
    <p class="holder-name">Marcus Lind</p>
    <span class="rule rule--left"></span>
    <p class="holder-role">Managing Director</p>
    <span class="rule rule--right"></span>
    <footer class="contact-band">
      <address class="contact-address">
        <div>Level 12, 48 Harbour Rd</div>
        <div>Brisbane QLD 4000</div>
        <div>Australia</div>
      </address>
      <div class="contact-lines">
        <div>M: +61 400 555 172</div>
        <div>P: +61 7 3000 4826</div>
        <div>E: mlind@kalderestates.com</div>
      </div>
    </footer>
  </article>
</body>
</html>
```